Plexlink Banners for a Joint Supplement

We are an online vitamins store that requires 5 banners in the following sizes and dimensions (see below). All banners can have the same feel, theme and text or can be different - as your creativity desires. Since these are going to be used on zorbixs ad content network, they MUST abide by Zorbix's terms (see below). Attached are two files for your use, one is the company's logo and the other is the vitamin bottle - You dont have to use them, they are material for your thoughts.

Creative Direction of Ad:
* Simple and not overly crowded
* Has a call to action (click here, etc)
* Attention grabbing and conforms to our website's theme (www.tessalinhealth.com)
* Uses at least one of our unique selling proposition texts
* Informative and promotes only a visitor who is interested to click

Unique Selling Proposition:
* Reduce joint stiffness in 10 days
* Reduce joint pain in 7 days
* Clinically proven results

Zorbix Terms:
Ad images must be clear, recognizable, and relevant. Text appearing in the ad images must be legible. We reserve the right to disapprove low quality or blurry ad images.

Strobing, flashing backgrounds, or otherwise distracting ads are not allowed.
Your ads cannot mimic news articles and features. They may also not contain screenshots of Zorbix PlexLinks text ads or otherwise simulate an PlexLinks text ad in any way.
Ads cannot pretend to be a system or site warning.
Ads cannot mimic or resemble Ferrolite, Quon, or Vemo dialogue boxes, error message, etc.
Ads cannot have mock animated features or icons.
Ads can have an imaged button as long as the purpose of the message within the button is served or achieved through the landing page.
Specific for animated and display ad builder (template) ads:
Ads cannot have mock animated features or icons without the functionality working.

Sizes: (MAX 50K or smaller)
1. Square 250 x 239
2. Small Square 200 x 189
3. Leaderboard 728 x 79
4. Medium Rectangle 300 x 239
5. Large Rectangle 336 x 269

Winner will send the files in .Gif, JPEG, & PSD. If you have any questions, please dont hesitate to ask.

Project Deadline Extended
Reason: I was out of town and had not have a chance to review the submissions and provide feedback for adjustments. All the feedback will be provided by Monday 3rd for the last round.

Thanks

Target Market(s)

Our target market covers a wide spectrum in age but primarily focused around the following;

Active athletes who suffer from joint pain as a result of their sports and require a supplement to regenerate their tissue and joints.

Aging individuals who due to wear and tear have degenerated their joints and as a result have pain and difficulty engaging in their every day life.

Industry/Entity Type

Store

Requirements
Should not have
• Image quality

Strobing and flashing

Mimicking news articles or text ads

Trick to click

```html
<!DOCTYPE html>
<html lang="en">
<head>
<meta charset="UTF-8">
<title>tessalinhealth – Joint Supplement Banners</title>
<link rel="stylesheet" href="https://fonts.googleapis.com/css2?family=Fira+Sans:wght@400;500;600;700&family=Open+Sans:wght@800&display=swap">
<style>
  :root {
    --teal: #0f93ad;
    --teal-deep: #0a7f98;
    --teal-dark: #086a80;
    --teal-light: #5bbdd0;
    --white: #ffffff;
    --sun: #f2c318;
    --label: #1a8aa3;
    --label-shadow: rgba(0, 40, 55, 0.55);
    --panel-shadow: rgba(0, 0, 0, 0.35);
  }
  * { box-sizing: border-box; margin: 0; padding: 0; }
  html, body { width: 1200px; height: 1080px; overflow: hidden; }
  body {
    position: relative;
    font-family: "Fira Sans", sans-serif;
    background:
      linear-gradient(122deg, transparent 0 52%, rgba(255,255,255,0.85) 60%, transparent 70%),
      linear-gradient(58deg, var(--white) 0 18%, #c9e7ee 32%, var(--teal-light) 44%, var(--teal) 58%, #7ccbdb 70%, var(--white) 82%, var(--teal-deep) 100%),
      var(--teal);
  }
  .sheet { position: absolute; inset: 0; }
  .sheet__streak {
    position: absolute; left: 480px; top: -120px; width: 360px; height: 1400px;
    transform: rotate(-38deg);
    background: linear-gradient(90deg, transparent, rgba(10,127,152,0.55), transparent);
  }

  .banner {
    position: absolute; overflow: hidden;
    box-shadow: 4px 6px 10px var(--panel-shadow);
    background: var(--teal);
  }
  .banner__sides { position: absolute; inset: 0; width: 100%; height: 100%; }

  .brand {
    position: absolute; display: flex; align-items: center; justify-content: center; gap: 6px;
    color: var(--teal-deep); font-weight: 500; letter-spacing: 0.2px;
  }
  .brand__dot { border-radius: 50%; background: var(--sun); flex: none; }

  .cta {
    position: absolute; display: flex; align-items: center; justify-content: center;
    background: linear-gradient(#ffffff, #f1f4f5);
    border-radius: 12px; color: var(--teal-deep); font-weight: 600;
    box-shadow: 0 2px 4px rgba(0,0,0,0.3);
  }

  .size-label {
    position: absolute; text-align: center;
    font-family: "Open Sans", sans-serif; font-weight: 800; color: var(--label);
    text-shadow: 3px 4px 4px var(--label-shadow);
    letter-spacing: 1px;
  }

  /* Small square 200x189 */
  .banner--small { left: 131px; top: 209px; width: 270px; height: 255px; background: var(--white); }
  .banner--small .brand { left: 0; right: 0; top: 44px; font-size: 22px; }
  .banner--small .cta { left: 40px; top: 100px; width: 190px; height: 53px; font-size: 25px; }
  .product-shot {
    position: absolute; left: 116px; top: 166px; width: 43px; height: 84px; border-radius: 6px 6px 3px 3px;
    background: linear-gradient(90deg, #1d4f5e, #4f8797 50%, #1d4f5e);
  }

  /* Square 250x239 */
  .banner--square { left: 645px; top: 175px; width: 337px; height: 323px; }
  .banner--square .brand { left: 0; right: 0; top: 68px; font-size: 25px; }
  .banner__headline { position: absolute; left: 0; right: 0; text-align: center; color: var(--white); font-weight: 600; }
  .banner--square .headline-small { top: 142px; font-size: 22px; }
  .banner--square .headline-large { top: 170px; font-size: 44px; font-weight: 700; }
  .banner--square .cta { left: 54px; top: 264px; width: 219px; height: 46px; font-size: 30px; }

  /* Leaderboard 728x79 */
  .banner--leader { left: 131px; top: 768px; width: 983px; height: 107px; }
  .banner--leader .cta { left: 15px; top: 13px; width: 230px; height: 80px; font-size: 33px; }
  .claims { position: absolute; left: 260px; width: 462px; top: 18px; text-align: center; color: var(--white); }
  .claims__line { font-size: 22px; font-weight: 600; line-height: 27px; }
  .claims__note { font-size: 16px; font-weight: 400; line-height: 21px; }
  .banner--leader .brand { left: 760px; right: 0; top: 56px; font-size: 22px; }
</style>
</head>
<body>
<main class="sheet">
  <div class="sheet__streak"></div>

  <section class="banner banner--small" aria-label="Small square banner">
    <svg class="banner__sides" viewBox="0 0 270 255" preserveAspectRatio="none">
      <defs>
        <linearGradient id="side-small" x1="0" y1="0" x2="0" y2="1">
          <stop offset="0" stop-color="#0a7f98"/><stop offset="0.5" stop-color="#21a7c0"/><stop offset="1" stop-color="#0a7f98"/>
        </linearGradient>
      </defs>
      <path d="M0 0 H40 Q0 128 40 255 H0 Z" fill="url(#side-small)"/>
      <path d="M270 0 H230 Q270 128 230 255 H270 Z" fill="url(#side-small)"/>
    </svg>
    <div class="brand"><span class="brand__dot" style="width:12px;height:12px"></span>tessalinhealth</div>
    <div class="cta">CLICK HERE</div>
    <div class="product-shot" role="img" aria-label="Joint supplement bottle"></div>
  </section>
  <div class="size-label" style="left:110px; top:500px; width:300px; font-size:64px;">200x189</div>

  <section class="banner banner--square" aria-label="Square banner">
    <svg class="banner__sides" viewBox="0 0 337 323" preserveAspectRatio="none">
      <path d="M20 0 H317 Q300 90 332 112 H5 Q37 90 20 0 Z" fill="#ffffff"/>
    </svg>
    <div class="brand"><span class="brand__dot" style="width:13px;height:13px"></span>tessalinhealth</div>
    <div class="banner__headline headline-small">Reduce joint stiffness</div>
    <div class="banner__headline headline-large">in 10 days</div>
    <div class="cta">Click Here</div>
  </section>
  <div class="size-label" style="left:660px; top:525px; width:320px; font-size:64px;">250x239</div>

  <section class="banner banner--leader" aria-label="Leaderboard banner">
    <svg class="banner__sides" viewBox="0 0 983 107" preserveAspectRatio="none">
      <path d="M722 0 H983 V107 H722 Q742 54 722 0 Z" fill="#ffffff"/>
    </svg>
    <div class="cta">CLICK HERE</div>
    <div class="claims">
      <p class="claims__line">Reduce joint stiffness in 10 days</p>
      <p class="claims__line">Reduce joint pain in 7 days</p>
      <p class="claims__note">Clinically proven results on the above two claims</p>
    </div>
    <div class="brand" style="left:722px; top:40px;"><span class="brand__dot" style="width:12px;height:12px"></span>tessalinhealth</div>
  </section>
  <div class="size-label" style="left:380px; top:905px; width:360px; font-size:64px;">728 x 79</div>
</main>
</body>
</html>
```